Design Large Inspirational Artwork with Long Quote

Design a large piece of art with a quote from Marcus Hallwell.

QUOTE
"The thing that's so interesting about being alive is that you're all in. No matter what you do, you're all in. This is gonna kill you, so I think you might as well play the most magnificent game you can while you're waiting. Because, do you have anything better to do? Why not pick the best thing possible that you could do? Because you're more powerful than you think, way more powerful than you think. I mean, God only knows what you are in the final analysis. You're blind to your own weaknesses, but you're also blind to your own strengths. How far could you take that if you stopped wasting time, and if you stopped lying, and if you oriented yourself to the highest possible good that you could conceive of and you committed to that? How much good could you do? Well, I would say: why don't you find out?"

SIZE
A high-resolution print size of 6' wide and 3' tall should provide ample space for both the quote and the accompanying artwork.

TYPOGRAPHY
Choose a bold, clean, and easily readable font for the quote. You could also experiment with different font sizes for certain words or phrases to emphasize their importance within the quote.

COLORS
Since the quote is thought-provoking and reflective, you might want to use a color palette that evokes a sense of introspection and depth. Consider using cool, calming colors like shades of blue, gray, or green. Alternatively, you can use a contrasting color scheme with a light background and dark text to make the quote stand out.

ARTWORK
Select / create / edit background artwork to complement the quote.
While a great design might be minimalistic and/or greyscale, I'd really like to see some full color options. This might be anything from photography or graphics inspired by the ideas in the text, to abstract colors or illustrations that feel like the sentiment expressed.
The art should capture your attention and encourage you to read the text. The art should be visually appealing, both at a distance and up close, regardless of whether the text is read.
Updates

Having trouble confirming the exact print size.

Still looking for printing solution and final size confirmation.

Target Market(s)

Personal, business, office

Industry/Entity Type

None

Font styles to use
Sans Serif
Script

Requirements
Must have
• Entire quote, legible text, modern design, attractive artwork, approx 6ft wide and 3ft tall
Nice to have
• Different font (sizes) for certain words or phrases to emphasize their importance within the quote.

```html
<!DOCTYPE html>
<html lang="en">
<head>
<meta charset="utf-8">
<title>All In — Quote Artwork Variants</title>
<link rel="stylesheet" href="https://fonts.googleapis.com/css2?family=Montserrat:wght@500;600;700&display=swap">
<style>
  :root {
    --sheet: #000000;
    --ink: #ffffff;
    --deep-1: #0a1d45;
    --deep-2: #1d4f86;
    --deep-3: #2f7bae;
    --light-1: #1f5e9c;
    --light-2: #3b8ac9;
    --light-3: #1aa0c9;
    --tag-bg: rgba(140, 190, 235, 0.45);
  }
  * { box-sizing: border-box; margin: 0; padding: 0; }
  html, body {
    width: 1200px; height: 1200px; overflow: hidden;
    background: var(--sheet);
  }
  .sheet { position: relative; width: 1200px; height: 1200px; }
  .artwork {
    position: absolute; left: 55px; width: 1090px; height: 544px;
    overflow: hidden;
    font-family: "Montserrat", sans-serif;
    color: var(--ink);
  }
  .artwork--deep { top: 42px; }
  .artwork--light { top: 614px; }
  .artwork__backdrop { position: absolute; inset: 0; width: 100%; height: 100%; }
  .quote {
    position: absolute; left: 112px; top: 62px; width: 666px;
    text-align: center; text-transform: uppercase;
    text-shadow: 0 1px 3px rgba(0, 20, 50, 0.55);
  }
  .quote__line {
    display: block; height: 25px; line-height: 25px;
    font-size: 13px; font-weight: 600; letter-spacing: 0.02em;
    white-space: nowrap;
  }
  .quote__line--mid { font-size: 16px; }
  .s { font-size: 11.5px; font-weight: 600; }
  .m { font-size: 14px; font-weight: 600; }
  .e { font-size: 17px; font-weight: 700; }
  .x { font-size: 19px; font-weight: 700; }
  .author {
    position: absolute; left: 828px; top: 448px;
    width: 199px; height: 33px; line-height: 33px;
    padding-left: 10px;
    background: var(--tag-bg);
    font-size: 19px; font-weight: 700; letter-spacing: 0.01em;
  }
</style>
</head>
<body>
<div class="sheet">

  <section class="artwork artwork--deep">
    <svg class="artwork__backdrop" role="img" aria-label="Abstract artwork of swirling translucent blue smoke ribbons and glowing bubbles on deep navy" viewBox="0 0 1090 544" preserveAspectRatio="none">
      <defs>
        <radialGradient id="deepGlow" cx="60%" cy="45%" r="75%">
          <stop offset="0" stop-color="var(--deep-3)"/>
          <stop offset="0.5" stop-color="var(--deep-2)"/>
          <stop offset="1" stop-color="var(--deep-1)"/>
        </radialGradient>
      </defs>
      <rect width="1090" height="544" fill="url(#deepGlow)"/>
    </svg>
    <div class="quote">
      <span class="quote__line">"<span class="s">The thing that's so</span> <span class="e">interesting</span> <span class="s">about being</span> <span class="e">alive</span> <span class="s">is that you're all in.</span></span>
      <span class="quote__line"><span class="m">No</span> <span class="x">matter</span> <span class="m">what you</span> <span class="x">do</span><span class="m">, you're all in.</span></span>
      <span class="quote__line"><span class="s">This is gonna</span> <span class="e">kill you</span><span class="s">, so I think you might as well play the most</span> <span class="e">magnificent</span></span>
      <span class="quote__line"><span class="e">game</span> <span class="s">you can while you're waiting.</span></span>
      <span class="quote__line"><span class="s">Because, do you have anything</span> <span class="e">better</span> <span class="s">to do?</span></span>
      <span class="quote__line"><span class="s">Why not pick</span> <span class="e">the best</span> <span class="s">thing</span> <span class="e">possible</span> <span class="s">that you could do?</span></span>
      <span class="quote__line quote__line--mid">Because you're more <span class="x">powerful</span> than you think, way more</span>
      <span class="quote__line quote__line--mid"><span class="x">powerful</span> than you think.</span>
      <span class="quote__line quote__line--mid">I mean, <span class="x">God</span> only knows what you are in the final analysis.</span>
      <span class="quote__line"><span class="m">You're blind to your own</span> <span class="x">weaknesses</span><span class="m">, but you're also blind to your</span></span>
      <span class="quote__line"><span class="m">own</span> <span class="x">strengths</span>.</span>
      <span class="quote__line"><span class="s">How far could you take that if you</span> <span class="e">stopped wasting time</span>,</span>
      <span class="quote__line"><span class="s">and if you</span> <span class="e">stopped lying</span><span class="s">, and if you</span> <span class="e">oriented yourself</span> <span class="s">to</span> <span class="e">the highest</span></span>
      <span class="quote__line"><span class="m">possible good</span></span>
      <span class="quote__line"><span class="m">that you could</span> <span class="e">conceive</span> <span class="m">of and you</span> <span class="e">committed</span> <span class="m">to that?</span></span>
      <span class="quote__line"><span class="m">How much</span> <span class="e">good</span> <span class="m">could you do?</span></span>
      <span class="quote__line quote__line--mid">Well, I would say: <span class="x">why don't you find out?</span>"</span>
    </div>
    <div class="author">Marcus Hallwell</div>
  </section>

  <section class="artwork artwork--light">
    <svg class="artwork__backdrop" role="img" aria-label="Abstract artwork of swirling translucent blue smoke ribbons and glowing bubbles on bright ocean blue" viewBox="0 0 1090 544" preserveAspectRatio="none">
      <defs>
        <linearGradient id="lightGlow" x1="0" y1="0" x2="1" y2="1">
          <stop offset="0" stop-color="var(--light-1)"/>
          <stop offset="0.5" stop-color="var(--light-2)"/>
          <stop offset="1" stop-color="var(--light-3)"/>
        </linearGradient>
      </defs>
      <rect width="1090" height="544" fill="url(#lightGlow)"/>
    </svg>
    <div class="quote">
      <span class="quote__line">"<span class="s">The thing that's so</span> <span class="e">interesting</span> <span class="s">about being</span> <span class="e">alive</span> <span class="s">is that you're all in.</span></span>
      <span class="quote__line"><span class="m">No</span> <span class="x">matter</span> <span class="m">what you</span> <span class="x">do</span><span class="m">, you're all in.</span></span>
      <span class="quote__line"><span class="s">This is gonna</span> <span class="e">kill you</span><span class="s">, so I think you might as well play the most</span> <span class="e">magnificent</span></span>
      <span class="quote__line"><span class="e">game</span> <span class="s">you can while you're waiting.</span></span>
      <span class="quote__line"><span class="s">Because, do you have anything</span> <span class="e">better</span> <span class="s">to do?</span></span>
      <span class="quote__line"><span class="s">Why not pick</span> <span class="e">the best</span> <span class="s">thing</span> <span class="e">possible</span> <span class="s">that you could do?</span></span>
      <span class="quote__line quote__line--mid">Because you're more <span class="x">powerful</span> than you think, way more</span>
      <span class="quote__line quote__line--mid"><span class="x">powerful</span> than you think.</span>
      <span class="quote__line quote__line--mid">I mean, <span class="x">God</span> only knows what you are in the final analysis.</span>
      <span class="quote__line"><span class="m">You're blind to your own</span> <span class="x">weaknesses</span><span class="m">, but you're also blind to your</span></span>
      <span class="quote__line"><span class="m">own</span> <span class="x">strengths</span>.</span>
      <span class="quote__line"><span class="s">How far could you take that if you</span> <span class="e">stopped wasting time</span>,</span>
      <span class="quote__line"><span class="s">and if you</span> <span class="e">stopped lying</span><span class="s">, and if you</span> <span class="e">oriented yourself</span> <span class="s">to</span> <span class="e">the highest</span></span>
      <span class="quote__line"><span class="m">possible good</span></span>
      <span class="quote__line"><span class="m">that you could</span> <span class="e">conceive</span> <span class="m">of and you</span> <span class="e">committed</span> <span class="m">to that?</span></span>
      <span class="quote__line"><span class="m">How much</span> <span class="e">good</span> <span class="m">could you do?</span></span>
      <span class="quote__line quote__line--mid">Well, I would say: <span class="x">why don't you find out?</span>"</span>
    </div>
    <div class="author">Marcus Hallwell</div>
  </section>

</div>
</body>
</html>
```